THis will be a flyer to post around town for our Big Buck Contest. Here are the rules (which can be in small print). It should appeal to hunters. We are in Texas.

2014-2015 BIG BUCK CONTEST
OFFICIAL RULES:
1. Eligible hunters must be signed in and have $20 entry fee paid between November 1, 2014 - ____________________. Hunters may enter online @ www.brindlecreekhub.org or stop by The Pecan Hollow Area Chamber of Commerce for an entry form @ 418 E. Juniper Ave. on the square in Pecan Hollow.
2. Deer must be a whitetail buck killed during the general hunting season.
3. Bucks killed within a deer-proof fence or any other confined areas are not eligible to enter contest. Bucks that were EVER kept inside a pen for breeding purposes or any other reason are NOT allowed. Bucks that are tagged or tattooed are NOT allowed. Bucks cannot have been raised in a fenced in area and released. Bucks considered tame, domesticated or pet are NOT allowed.
4. Bucks must be properly tagged according to Texas State Law when brought in for measurement. Hunter must present valid hunting license and contest entry for to the official measurer.
5. Hunters attempting to cheat in the BIG BUCK CONTEST or violating Texas Game Laws are disqualified and barred from entering this contest for a period of time to be determined by the contest committee.
6. NO MORE than 1 prize will be awarded to any registered hunter. A hunter’s second buck is valid if it outscores first buck.
7. All entries must be brought in by the rightful. Any attempts to alter or enhance the horns in any from will be grounds for disqualification WITHOUT refund.
8. You must enter your buck in the contest within 72 hours of kill, unless prior arrangements have been made.

Measurements Guidelines:
For measurement, the hunter must bring the ENTIRE BODY of the field dressed animal to one of the official measurers.

Total $25.00
_____ Check ______ Money Order _____ Cashier Check
*** Please DO NOT DROP OFF OF MAIL CASH***

DROP OFF AT OR MAIL TO:

The Pecan Hollow Area Chamber of Commerce
418 E. Juniper Ave
Pecan Hollow, TX 76312

PRIZES:
1. Velmon Strouth Taxidermy - Shoulder Mount (donated)
>
> 2. 45 quart Kodo cooler sponsored by Ridgeway Timber and Fellowship of the Plains
>
> 3. 500 lbs of deer corn sponsored by Tanning Feed.

Target Market(s)

Texas deer hunters

Industry/Entity Type

Town

Requirements
Must have
• rules
• Fee amount $20
• Pecan Hollow Area Chamber of Commerce

```html
<!DOCTYPE html>
<html lang="en">
<head>
<meta charset="utf-8">
<title>2014-2015 Big Buck Contest</title>
<link rel="stylesheet" href="https://fonts.googleapis.com/css2?family=Rye&family=Oswald:wght@400;600;700&family=Roboto+Condensed:wght@400;700&display=swap">
<style>
:root{
  --wood-1:#5e4f40;
  --wood-2:#76675a;
  --wood-3:#8b7d6d;
  --wood-seam:#2f261e;
  --ink-light:#f4efe6;
  --note:#f4dc1e;
  --note-edge:#d9bf10;
  --note-ink:#2a2418;
  --pin:#c8262b;
  --pin-shine:#f07a7a;
  --photo-dark:#2e3d22;
  --photo-light:#6f7f4a;
}
*{box-sizing:border-box;margin:0;padding:0}
html,body{width:900px;height:1200px;overflow:hidden;background:#222}
.flyer{
  position:relative;width:900px;height:1200px;overflow:hidden;
  background:
    radial-gradient(ellipse at 50% 40%, rgba(0,0,0,0) 45%, rgba(0,0,0,.45) 100%),
    repeating-linear-gradient(90deg,
      var(--wood-seam) 0 4px,
      var(--wood-1) 4px 30px,
      var(--wood-2) 30px 80px,
      var(--wood-3) 80px 118px,
      var(--wood-2) 118px 150px);
  color:var(--ink-light);
}
.chamber{
  position:absolute;top:22px;left:0;width:100%;text-align:center;
  font-family:'Oswald',sans-serif;font-weight:600;font-size:26px;letter-spacing:2px;
  text-shadow:0 2px 4px rgba(0,0,0,.6);
}
.season,.big-buck,.contest-word{
  position:absolute;left:0;width:100%;text-align:center;
  font-family:'Rye',serif;text-shadow:0 4px 8px rgba(0,0,0,.55);
}
.season{top:70px;font-size:112px;line-height:1}
.big-buck{top:195px;font-size:158px;line-height:1;letter-spacing:2px}
.contest-word{top:350px;font-size:74px;line-height:1;letter-spacing:14px}
.deer-photo{
  position:absolute;left:118px;top:448px;width:275px;height:232px;
  background:linear-gradient(160deg,var(--photo-dark),var(--photo-light) 55%,var(--photo-dark));
  box-shadow:0 6px 14px rgba(0,0,0,.6);
}
.pin{position:absolute;width:24px;height:24px;border-radius:50%;
  background:radial-gradient(circle at 35% 35%,var(--pin-shine),var(--pin) 55%,#7a1214);
  box-shadow:2px 3px 4px rgba(0,0,0,.5)}
.pin-photo{left:110px;top:436px}
.prize-note{
  position:absolute;left:480px;top:452px;width:392px;height:360px;
  background:var(--note);border-bottom:4px solid var(--note-edge);
  transform:rotate(-2deg);box-shadow:0 8px 16px rgba(0,0,0,.55);
  padding:34px 26px 20px 34px;color:var(--note-ink);
  font-family:'Oswald',sans-serif;
}
.pin-note{left:595px;top:440px}
.prize{margin-bottom:14px}
.prize-rank{font-weight:700;font-size:30px;line-height:1.05}
.prize-rank sup{font-size:17px}
.prize-detail{font-weight:600;font-size:20px;line-height:1.15;text-transform:uppercase}
.rules{
  position:absolute;left:30px;top:858px;width:440px;
  font-family:'Roboto Condensed',sans-serif;font-size:9.6px;line-height:1.22;
  text-shadow:0 1px 2px rgba(0,0,0,.7);
}
.rules h3,.side h3{font-family:'Oswald',sans-serif;font-weight:600;font-size:13px;letter-spacing:.5px;margin-bottom:3px}
.rules ol{padding-left:12px}
.rules li{margin-bottom:2px}
.side{
  position:absolute;left:500px;width:370px;
  font-family:'Roboto Condensed',sans-serif;font-size:10.5px;line-height:1.3;
  text-shadow:0 1px 2px rgba(0,0,0,.7);
}
.measure{top:868px}
.payment{top:950px}
.payment .options{display:flex;gap:14px;margin-top:2px}
.payment .warn{margin-top:3px;font-weight:700}
.dropoff{top:1010px}
.dropoff p{font-size:11px}
</style>
</head>
<body>
<main class="flyer">
  <div class="chamber">PECAN HOLLOW AREA CHAMBER OF COMMERCE</div>
  <h1 class="season">2014-2015</h1>
  <div class="big-buck">BIG BUCK</div>
  <div class="contest-word">CONTEST</div>

  <div class="deer-photo" role="img" aria-label="Photo of a whitetail buck standing at the edge of green brush"></div>
  <span class="pin pin-photo"></span>

  <section class="prize-note">
    <div class="prize">
      <div class="prize-rank">1<sup>ST</sup> PRIZE</div>
      <div class="prize-detail">Velmon Strouth Taxidermy - Shoulder Mount (Donated)</div>
    </div>
    <div class="prize">
      <div class="prize-rank">2<sup>ND</sup> PRIZE</div>
      <div class="prize-detail">45 Quart Kodo Cooler Sponsored by Ridgeway Timber and Fellowship of the Plains</div>
    </div>
    <div class="prize">
      <div class="prize-rank">3<sup>RD</sup> PRIZE</div>
      <div class="prize-detail">500 lbs of Deer Corn Sponsored by Tanning Feed</div>
    </div>
  </section>
  <span class="pin pin-note"></span>

  <section class="rules">
    <h3>OFFICIAL RULES:</h3>
    <ol>
      <li>Eligible hunters must be signed in and have $20 entry fee paid between November 1, 2014 - ____________. Hunters may enter online @ www.brindlecreekhub.org or stop by The Pecan Hollow Area Chamber of Commerce for an entry form @ 418 E. Juniper Ave. on the square in Pecan Hollow.</li>
      <li>Deer must be a whitetail buck killed during the general hunting season.</li>
      <li>Bucks killed within a deer-proof fence or any other confined areas are not eligible to enter contest. Bucks that were EVER kept inside a pen for breeding purposes or any other reason are NOT allowed. Bucks that are tagged or tattooed are NOT allowed. Bucks cannot have been raised in a fenced in area and released. Bucks considered tame, domesticated or pet are NOT allowed.</li>
      <li>Bucks must be properly tagged according to Texas State Law when brought in for measurement. Hunter must present valid hunting license and contest entry form to the official measurer.</li>
      <li>Hunters attempting to cheat in the BIG BUCK CONTEST or violating Texas Game Laws are disqualified and barred from entering this contest for a period of time to be determined by the contest committee.</li>
      <li>NO MORE than 1 prize will be awarded to any registered hunter. A hunter's second buck is valid if it outscores first buck.</li>
      <li>All entries must be brought in by the rightful hunter. Any attempts to alter or enhance the horns in any form will be grounds for disqualification WITHOUT refund.</li>
      <li>You must enter your buck in the contest within 72 hours of kill, unless prior arrangements have been made.</li>
    </ol>
  </section>

  <section class="side measure">
    <h3>MEASUREMENTS GUIDELINES:</h3>
    <p>For measurement, the hunter must bring the ENTIRE BODY of the field dressed animal to one of the official measurers.</p>
  </section>

  <section class="side payment">
    <p><strong>Total $20.00</strong></p>
    <div class="options"><span>____ Check</span><span>____ Money Order</span><span>____ Cashier Check</span></div>
    <p class="warn">*** Please DO NOT DROP OFF OR MAIL CASH ***</p>
  </section>

  <section class="side dropoff">
    <h3>DROP OFF AT OR MAIL TO:</h3>
    <p>The Pecan Hollow Area Chamber of Commerce<br>418 E. Juniper Ave<br>Pecan Hollow, TX 76312</p>
  </section>
</main>
</body>
</html>
```